Single-page, simple & clean, departure board web app

TrellisHop.com provides easy to use train schedule information in Chicago, IL between downtown and Hyde Park. The site has been around for about 3 years and the design has not changed since the weekend hackathon at which it was created. Now, it has a solid user base and is in dire need of a fresh design.
The design should be super-clean and intuitive. It is used by the type of people who love the style and personality of sites like Gravlox. The design should incorporate the maroon color that is used extensively on the existing site. The main features are (1) the train depart times, (2) the fact that different stations can be selected as departure/arrival, (3) the fact that a user can click "earlier trains" or "later trains" to quickly scan the times.
This is a single-page web app that displays static content. The design should reflect that 100% of the users time is spent on the single page. There is no "sign up" process or external aspect. All focus should be used to design the best possible display of train times.
Target Market(s)
24-30 yr old, middle to upper income, opinionated, heavily international
Look and feel
Each slider illustrates characteristics of the customer's brand and the style your logo design should communicate.

```html
<!DOCTYPE html>
<html lang="en">
<head>
<meta charset="utf-8">
<title>TrellisHop – Train Times</title>
<link rel="stylesheet" href="https://fonts.googleapis.com/css2?family=Source+Sans+3:wght@400;600&display=swap">
<style>
:root{
  --ink:#333;
  --muted:#6a6a6a;
  --navy:#1d4a7a;
  --bar:#0a6bb5;
  --bar-dark:#0660a6;
  --panel-line:#cfd4d8;
  --page:#ffffff;
  --foot:#e3e3e3;
  --tab-top:#f7f7f7;
  --tab-bottom:#dcdcdc;
  --tab-line:#9a9a9a;
  --active-top:#4a4a4a;
  --active-bottom:#0d0d0d;
}
*{box-sizing:border-box;margin:0;padding:0}
html,body{width:750px;height:1200px;overflow:hidden;background:var(--page)}
body{position:relative;font-family:"Source Sans 3",sans-serif;color:var(--ink)}
.site-header{position:absolute;left:0;top:0;width:750px;height:77px;border-bottom:1px solid #ddd;background:linear-gradient(#fff,#fafafa)}
.brand{position:absolute;left:29px;top:20px;font-size:25px;font-weight:600;color:#666;letter-spacing:.2px}
.tagline{position:absolute;left:207px;top:25px;font-size:10.5px;line-height:16px;color:var(--muted)}
.board{position:absolute;left:14px;width:721px;border:1px solid var(--panel-line);border-radius:4px;background:#fff;box-shadow:0 1px 3px rgba(0,0,0,.08)}
.board-bar{position:absolute;left:2px;right:2px;top:3px;height:34px;background:linear-gradient(var(--bar),var(--bar-dark));border-radius:2px;color:#fff}
.board-title{position:absolute;left:0;right:0;top:5px;text-align:center;font-size:19px}
.board-title svg{vertical-align:-5px;margin-right:6px}
.nav{position:absolute;top:10px;font-size:10px;display:flex;align-items:center;gap:8px}
.nav.earlier{left:13px}
.nav.later{right:13px}
.nav .dot{width:16px;height:16px;border-radius:50%;display:inline-block}
.nav.earlier .dot{background:#eee}
.nav.later .dot{background:#222}
.tab{position:absolute;height:30px;border:1px solid var(--tab-line);border-radius:2px;background:linear-gradient(var(--tab-top),var(--tab-bottom));font-size:12px;text-align:center;line-height:28px;color:#222}
.tab.active{background:linear-gradient(var(--active-top),var(--active-bottom));border-color:#000;color:#fff}
.trip{position:absolute;left:0;width:100%}
.trip-icon{position:absolute;left:20px;top:2px}
.trip-name{position:absolute;left:56px;top:0;font-size:12px}
.trip-times{position:absolute;left:269px;top:0;font-size:12px;line-height:15.7px}
.trip-times .depart-label,.trip-times .depart-time{color:var(--navy)}
.trip-times .stop{padding-left:3px}
.divider{position:absolute;left:60px;right:60px;height:14px;background:radial-gradient(ellipse at center top,rgba(0,0,0,.07),rgba(0,0,0,0) 70%)}
.promos{position:absolute;left:127px;top:1063px;font-size:9.5px;line-height:19.6px;color:#444}
.site-footer{position:absolute;left:0;top:1130px;width:750px;height:70px;background:var(--foot);border-top:1px solid #ccc;text-align:center;font-size:9.5px;color:#333}
.site-footer p{position:absolute;left:0;right:0}
</style>
</head>
<body>
<header class="site-header">
  <div class="brand">TrellisHop</div>
  <p class="tagline">Lakeline Electric between Downtown Chicago and Lakeside Campus<br>Designed for home, school, and mobile access</p>
</header>

<section class="board" style="top:96px;height:466px">
  <div class="board-bar">
    <div class="nav earlier"><span class="dot"></span>Earlier Trains</div>
    <div class="board-title"><svg width="38" height="22" viewBox="0 0 38 22"><rect x="2" y="3" width="34" height="15" rx="5" fill="#e8e8e8"/><rect x="6" y="6" width="24" height="5" rx="1" fill="#2a3b4a"/><rect x="2" y="13" width="34" height="3" fill="#3a8f3a"/><circle cx="9" cy="19" r="2" fill="#222"/><circle cx="29" cy="19" r="2" fill="#222"/></svg>To Lakeside Campus</div>
    <div class="nav later">Later Trains<span class="dot"></span></div>
  </div>
  <div class="tab active" style="left:34px;top:56px;width:170px">From Millenium</div>
  <div class="tab" style="left:267px;top:56px;width:170px">From Van buren</div>
  <div class="tab" style="left:507px;top:56px;width:170px">From&nbsp; 11th</div>

  <div class="trip" style="top:127px">
    <svg class="trip-icon" width="30" height="22" viewBox="0 0 30 22"><path d="M2 18 L6 8 Q9 3 16 3 L28 3 L26 14 Q24 19 18 19 Z" fill="#ddd" stroke="#444" stroke-width="1.3"/><path d="M8 9 L26 6" stroke="#444" stroke-width="2"/></svg>
    <span class="trip-name">Train #309</span>
    <p class="trip-times"><span class="depart-label">Depart:</span> <span class="depart-time">7:15</span> am from Millennium Station<br><span class="stop">Arrive:&nbsp; 7:29 am at 51st-53rd Street</span><br><span class="stop">Arrive:&nbsp; 7:31 am at 55th-56th-57th Street</span><br><span class="stop">Arrive:&nbsp; 7:33 am at 59th Street</span></p>
  </div>
  <div class="divider" style="top:204px"></div>
  <div class="trip" style="top:248px">
    <svg class="trip-icon" width="30" height="22" viewBox="0 0 30 22"><path d="M2 18 L6 8 Q9 3 16 3 L28 3 L26 14 Q24 19 18 19 Z" fill="#ddd" stroke="#444" stroke-width="1.3"/><path d="M8 9 L26 6" stroke="#444" stroke-width="2"/></svg>
    <span class="trip-name">Train #111</span>
    <p class="trip-times" style="top:-7px"><span class="depart-label">Depart:</span> <span class="depart-time">7:48</span> am from Millennium Station<br><span class="stop">Arrive:&nbsp; 8:00 am at 51st-53rd Street</span><br><span class="stop">Arrive:&nbsp; 8:02 am at 55th-56th-57th Street</span><br><span class="stop">Arrive:&nbsp; 8:04 am at 59th Street</span></p>
  </div>
  <div class="divider" style="top:332px"></div>
  <div class="trip" style="top:376px">
    <svg class="trip-icon" width="30" height="22" viewBox="0 0 30 22"><path d="M2 18 L6 8 Q9 3 16 3 L28 3 L26 14 Q24 19 18 19 Z" fill="#ddd" stroke="#444" stroke-width="1.3"/><path d="M8 9 L26 6" stroke="#444" stroke-width="2"/></svg>
    <span class="trip-name">Train #313</span>
    <p class="trip-times" style="top:-7px"><span class="depart-label">Depart:</span> <span class="depart-time">8.20</span> am from Millennium Station<br><span class="stop">Arrive:&nbsp; 8:34 am at 51st-53rd Street</span><br><span class="stop">Arrive:&nbsp; 8:36 am at 55th-56th-57th Street</span><br><span class="stop">Arrive:&nbsp; 8:38 am at 59th Street</span></p>
  </div>
</section>

<section class="board" style="top:585px;height:466px">
  <div class="board-bar">
    <div class="nav earlier"><span class="dot"></span>Earlier Trains</div>
    <div class="board-title"><svg width="38" height="22" viewBox="0 0 38 22"><rect x="2" y="3" width="34" height="15" rx="5" fill="#e8e8e8"/><rect x="6" y="6" width="24" height="5" rx="1" fill="#2a3b4a"/><rect x="2" y="13" width="34" height="3" fill="#3a8f3a"/><circle cx="9" cy="19" r="2" fill="#222"/><circle cx="29" cy="19" r="2" fill="#222"/></svg>To Downtown</div>
    <div class="nav later">Later Trains<span class="dot"></span></div>
  </div>
  <div class="tab" style="left:12px;top:55px;width:163px">From 51st - 53rd</div>
  <div class="tab" style="left:188px;top:55px;width:163px">From&nbsp; 55th - 57th</div>
  <div class="tab active" style="left:365px;top:55px;width:163px">From 59th</div>
  <div class="tab" style="left:545px;top:55px;width:163px">From&nbsp; 57th or 59th</div>

  <div class="trip" style="top:127px">
    <svg class="trip-icon" width="30" height="22" viewBox="0 0 30 22"><path d="M2 18 L6 8 Q9 3 16 3 L28 3 L26 14 Q24 19 18 19 Z" fill="#ddd" stroke="#444" stroke-width="1.3"/><path d="M8 9 L26 6" stroke="#444" stroke-width="2"/></svg>
    <span class="trip-name">Train #308</span>
    <p class="trip-times"><span class="depart-label">Depart:</span> <span class="depart-time">7:30</span> am from 59th Street<br><span class="stop">Arrive:&nbsp; 7:43 am at 11th Street</span><br><span class="stop">Arrive:&nbsp; 7:46 am at Van Buren Street</span><br><span class="stop">Arrive:&nbsp; 7:49 am at Millennium Station</span></p>
  </div>
  <div class="divider" style="top:202px"></div>
  <div class="trip" style="top:248px">
    <svg class="trip-icon" width="30" height="22" viewBox="0 0 30 22"><path d="M2 18 L6 8 Q9 3 16 3 L28 3 L26 14 Q24 19 18 19 Z" fill="#ddd" stroke="#444" stroke-width="1.3"/><path d="M8 9 L26 6" stroke="#444" stroke-width="2"/></svg>
    <span class="trip-name">Train #210</span>
    <p class="trip-times" style="top:-7px"><span class="depart-label">Depart:</span> <span class="depart-time">7:53</span> am from 59th Street<br><span class="stop">Arrive:&nbsp; 8:02 am at 11th Street</span><br><span class="stop">Arrive:&nbsp; 8:04 am at Van Buren Street</span><br><span class="stop">Arrive:&nbsp; 8:07 am at Millennium Station</span></p>
  </div>
  <div class="divider" style="top:331px"></div>
  <div class="trip" style="top:376px">
    <svg class="trip-icon" width="30" height="22" viewBox="0 0 30 22"><path d="M2 18 L6 8 Q9 3 16 3 L28 3 L26 14 Q24 19 18 19 Z" fill="#ddd" stroke="#444" stroke-width="1.3"/><path d="M8 9 L26 6" stroke="#444" stroke-width="2"/></svg>
    <span class="trip-name">Train #310</span>
    <p class="trip-times" style="top:-7px"><span class="depart-label">Depart:</span> <span class="depart-time">8.00</span> am from 59th Street<br><span class="stop">Arrive:&nbsp; 8:13 am at 11th Street</span><br><span class="stop">Arrive:&nbsp; 8:16 am at Van Buren Street</span><br><span class="stop">Arrive:&nbsp; 8:19 am at Millennium Station</span></p>
  </div>
</section>

<aside class="promos">
  New York Externships Hands-On Clinicals for FMGs Free Consultation &amp; Doc. Revision www.clinicpathway.com<br>
  2&amp;3 BR New York Apartment River View | Marble Baths | Parking Indoor pool | New Bldg AllAmenities WillowCourtHomes.com<br>
  212 Harbor Row NYC Luxury Condominium Residences Harbor Row at 61st Street New York www.212harborrow.com
</aside>

<footer class="site-footer">
  <p style="top:9px">Train Schedule Last Updated: January 15, 2012</p>
  <p style="top:29px">Terms and Conditions of Use | Questions or Comments</p>
  <p style="top:49px;font-size:8.5px">© Copyright 2012 trellishop.com. All rights reserved.</p>
</footer>
</body>
</html>
```